Ostrel Appraisals BV business cards (a financial services company)

I am looking for a business card design that stands out in the financial advisory field of business & intellectual property valuation. The business card design should be conservative, yet different. Address details have changed since the attached business card. New address is:

Molenvlietkade 27
4817 KT Leiden
The Netherlands

Telephone number remains the same.

```html
<!DOCTYPE html>
<html lang="en">
<head>
<meta charset="utf-8">
<title>Ostrel Appraisals BV – Business Cards</title>
<link href="https://fonts.googleapis.com/css2?family=Ubuntu:wght@400;500;700&display=swap" rel="stylesheet">
<style>
  :root {
    --page-bg: #e4e5e8;
    --card-white: #ffffff;
    --card-dark: #232323;
    --brand-grey: #8c8c8c;
    --text-light: #ffffff;
    --card-shadow: 0 10px 28px rgba(0, 0, 0, 0.22);
  }
  * { box-sizing: border-box; margin: 0; padding: 0; }
  html, body {
    width: 1200px;
    height: 1000px;
    overflow: hidden;
    background: var(--page-bg);
    font-family: "Ubuntu", sans-serif;
  }
  .sheet {
    position: relative;
    width: 1200px;
    height: 1000px;
  }
  .card {
    position: absolute;
    left: 250px;
    width: 700px;
    height: 400px;
    border-radius: 22px;
    overflow: hidden;
    box-shadow: var(--card-shadow);
  }
  .card--front {
    top: 50px;
    background: var(--card-white);
  }
  .card--back {
    top: 540px;
    background: var(--card-dark);
  }

  /* brand name */
  .brand {
    display: flex;
    align-items: center;
    gap: 14px;
    color: var(--brand-grey);
    font-weight: 400;
    text-transform: uppercase;
    letter-spacing: 0.04em;
    white-space: nowrap;
  }
  .brand__square {
    width: 22px;
    height: 22px;
    background: var(--brand-grey);
    flex: none;
  }
  .card--front .brand {
    position: absolute;
    left: 0;
    right: 0;
    top: 160px;
    justify-content: center;
    font-size: 36px;
  }
  .card--front .website {
    position: absolute;
    left: 0;
    right: 0;
    top: 300px;
    text-align: center;
    font-size: 17px;
    letter-spacing: 0.22em;
    color: var(--brand-grey);
  }

  /* back side */
  .back__panel {
    position: absolute;
    inset: 0;
    width: 700px;
    height: 400px;
  }
  .card--back .brand {
    position: absolute;
    left: 34px;
    top: 222px;
    font-size: 21px;
    gap: 10px;
  }
  .card--back .brand__square {
    width: 16px;
    height: 16px;
  }
  .contact {
    position: absolute;
    right: 40px;
    top: 120px;
    text-align: right;
    color: var(--text-light);
  }
  .contact__name {
    font-size: 21px;
    font-weight: 700;
  }
  .contact__role {
    font-size: 15px;
    margin-top: 4px;
  }
  .contact__address {
    font-size: 15px;
    line-height: 1.4;
    margin-top: 14px;
  }
  .contact__list {
    list-style: none;
    margin-top: 16px;
    font-size: 15px;
    line-height: 1.75;
  }
  .contact__list li {
    display: flex;
    align-items: center;
    justify-content: flex-end;
    gap: 10px;
  }
  .contact__icon {
    width: 15px;
    height: 15px;
    flex: none;
  }
</style>
</head>
<body>
<main class="sheet">

  <section class="card card--front" aria-label="Business card front">
    <div class="brand">
      <span class="brand__square"></span>
      <span class="brand__name">Ostrel Appraisals</span>
    </div>
    <p class="website">www.ostrelappraisals.com</p>
  </section>

  <section class="card card--back" aria-label="Business card back">
    <svg class="back__panel" viewBox="0 0 700 400" aria-hidden="true">
      <path d="M0,150 L170,28 Q212,0 258,0 Q318,0 328,48 L388,400 L0,400 Z" fill="#ffffff"/>
    </svg>

    <div class="brand">
      <span class="brand__square"></span>
      <span class="brand__name">Ostrel Appraisals</span>
    </div>

    <div class="contact">
      <p class="contact__name">Marten Vlieg, CFA, ASA, RV</p>
      <p class="contact__role">Managing Director</p>
      <p class="contact__address">Molenvlietkade 27<br>4817 KT Leiden The Netherlands</p>
      <ul class="contact__list">
        <li>+31 (0)70 318 4426
          <svg class="contact__icon" viewBox="0 0 16 16" aria-hidden="true">
            <path d="M3.5 1.5 L6 1.5 L7 5 L5.3 6.2 Q6.5 9.2 9.8 10.7 L11 9 L14.5 10 L14.5 12.5 Q14 14.5 12 14.5 Q2 13.5 1.5 4 Q1.5 2 3.5 1.5 Z" fill="#ffffff"/>
          </svg>
        </li>
        <li>mvlieg@ostrelappraisals.com
          <svg class="contact__icon" viewBox="0 0 16 16" aria-hidden="true">
            <rect x="1" y="3" width="14" height="10" rx="1" fill="#ffffff"/>
            <path d="M2 4 L8 9 L14 4" fill="none" stroke="#232323" stroke-width="1.5"/>
          </svg>
        </li>
        <li>www.ostrelappraisals.com
          <svg class="contact__icon" viewBox="0 0 16 16" aria-hidden="true">
            <circle cx="8" cy="8" r="6.5" fill="#ffffff"/>
            <ellipse cx="8" cy="8" rx="2.8" ry="6.5" fill="none" stroke="#232323" stroke-width="1"/>
            <line x1="1.5" y1="8" x2="14.5" y2="8" stroke="#232323" stroke-width="1"/>
          </svg>
        </li>
      </ul>
    </div>
  </section>

</main>
</body>
</html>
```